New business card, letter head, email signature and Portfolio for our Security company.

We are an Elite security company that provides a top quality manpower services to protect high rise buildings, retail and all type of properties and would like a new business card/logo look.

- We would like the spot UV design.
- Matt black (double sided).
- We would like to incorporate a royal blue colour (feel free to experiment with it).
- Feel free to try different lengths with the card to make it stand out more than a normal business card.
- We would like the logo to be an eagle eye in the background (shines when card is tilted slightly in the background, either on the front, back or both sides of the card). Image attached as an example of eye shape (colour to be either black or royal blue).
- MAVRIN OAK GUARD PATROLS PTY. LTD. and MOGP to be placed on one side of the card and on the other side of the card to have;

- Name in slightly bigger font than the position (directly on the bottom on the name).
- Mobile number
- Email address
- Website email address
- PO BOX address

Can we please have the files in a format that we can edit.

Reason: I need to consult my business partner with the designs so far and will make a decision from there.

Target Market(s)

Security Industry

Industry/Entity Type

Business

Contact Information for Business Card

- Mobile number
- Email address
- Website email address
- PO BOX address

Logo Text

MOGP and underneath the MOGP please add MAVRIN OAK GUARD PATROLS PTY. LTD.

Font styles to use
Other font styles liked:
• bold type font

Colors
0255a3
000000

Requirements
Must have
• We are an Elite security company that provides a top quality manpower services to protect high rise buildings, retail and all type of properties and would like a new business card/logo look.
• - We would like the spot UV design.
• - Matt black (double sided).
• - We would like to incorporate a royal blue colour (feel free to experiment with it).
• - Feel free to try different lengths with the card to make it stand out more than a normal business card.
• - We would like the logo to be an eagle eye in the background (shines when card is tilted slightly in the background, either on the front, back or both sides of the card). Image attached as an example of eye shape (colour to be either black or royal blue).
• - MAVRIN OAK GUARD PATROLS PTY. LTD. and MOGP to be placed on one side of the card and on the other side of the card to have;
• - Name in slightly bigger font than the position (directly on the bottom on the name).
• - Mobile number
• - Email address
• - Website email address
• - PO BOX address
• Can we please have the files in a format that we can edit.
Nice to have
• Feel free to try different lengths with the card to make it stand out more than a normal business card.
• Please find "URBAN JUNGLE" font attached and incorporate MOGP into the same style with building's inside the MOGP bold front also add MAVRIN into the bottom part of the S and follow on E - Elite on the bottom S - SECURITY on the bottom S - SERVICES on the bottom of each letter.
• other than that, I'll be happy with a bold modern font for the MOGP and MAVRIN OAK GUARD PATROLS in a bold and thinner font underneath.

```html
<!DOCTYPE html>
<html lang="en">
<head>
<meta charset="utf-8">
<title>Mavrin Oak Guard Patrols – Business Card</title>
<link rel="stylesheet" href="https://fonts.googleapis.com/css2?family=Michroma&family=Questrial&display=swap">
<style>
  :root {
    --royal-blue: #0255a3;
    --deep-blue: #0a3f82;
    --matt-black: #000000;
    --ink-black: #05070c;
    --white: #ffffff;
    --silver: #c9ccd2;
    --stripe-grey: #9ea3ab;
    --backdrop: #ececec;
    --faint-blue: rgba(20, 90, 175, 0.45);
    --icon-blue: #2f74c8;
  }
  * { margin: 0; padding: 0; box-sizing: border-box; }
  html, body {
    width: 1200px;
    height: 400px;
    overflow: hidden;
    background: var(--backdrop);
  }
  .canvas {
    position: relative;
    width: 1200px;
    height: 400px;
  }
  .card {
    position: absolute;
    top: 93px;
    width: 479px;
    height: 213px;
    overflow: hidden;
    background: linear-gradient(180deg, var(--deep-blue) 0%, #06295a 45%, var(--matt-black) 100%);
  }
  .card--front { left: 109px; }
  .card--back { left: 613px; }

  .front-panel {
    position: absolute;
    inset: 0;
  }
  .company-name {
    position: absolute;
    left: 21px;
    top: 141px;
    font-family: "Michroma", sans-serif;
    font-weight: 400;
    font-size: 15px;
    line-height: 19px;
    letter-spacing: 0.5px;
    color: var(--white);
  }
  .company-name .line { display: block; }
  .company-name .line--muted { color: var(--silver); }

  .brand-mark {
    position: absolute;
    left: 349px;
    top: 106px;
    transform: translate(-50%, -50%);
    font-family: "Michroma", sans-serif;
    font-size: 24px;
    color: var(--royal-blue);
    letter-spacing: 1px;
    white-space: nowrap;
  }

  .ghost-name {
    position: absolute;
    right: -14px;
    top: 4px;
    font-family: "Michroma", sans-serif;
    font-size: 50px;
    line-height: 70px;
    color: var(--faint-blue);
    letter-spacing: 2px;
  }
  .wordmark {
    position: absolute;
    left: 56px;
    top: 88px;
    width: 164px;
    text-align: center;
    color: var(--white);
    font-family: "Michroma", sans-serif;
  }
  .wordmark-title {
    font-size: 31px;
    line-height: 56px;
    letter-spacing: 0;
    white-space: nowrap;
  }
  .wordmark-sub {
    font-size: 6.3px;
    letter-spacing: 0.3px;
    margin-top: 8px;
    white-space: nowrap;
  }
  .contact {
    position: absolute;
    left: 235px;
    top: 87px;
    font-family: "Questrial", sans-serif;
    color: var(--white);
  }
  .contact-name {
    font-family: "Michroma", sans-serif;
    font-size: 11px;
    line-height: 14px;
    letter-spacing: 0.3px;
    margin-bottom: 2px;
  }
  .contact-list { list-style: none; }
  .contact-item {
    display: flex;
    align-items: center;
    gap: 6px;
    padding-left: 6px;
    font-size: 13px;
    line-height: 16px;
    color: #e8ecf3;
    white-space: nowrap;
  }
  .contact-icon {
    width: 8px;
    height: 8px;
    border-radius: 2px;
    background: var(--icon-blue);
    flex: none;
  }
  .contact-icon--none { background: transparent; }

  .base-stripes {
    position: absolute;
    left: 0;
    bottom: 0;
    width: 479px;
    height: 32px;
  }
</style>
</head>
<body>
<main class="canvas">

  <section class="card card--front" aria-label="Business card front">
    <svg class="front-panel" width="479" height="213" viewBox="0 0 479 213" aria-hidden="true">
      <path d="M479 0 H232 C208 45 206 145 276 213 H479 Z" fill="var(--white)"/>
    </svg>
    <p class="brand-mark">MOGP</p>
    <h1 class="company-name">
      <span class="line">MAVRIN</span>
      <span class="line">OAK GUARD</span>
      <span class="line line--muted">PATROLS</span>
    </h1>
  </section>

  <section class="card card--back" aria-label="Business card back">
    <p class="ghost-name" aria-hidden="true">MOGP</p>

    <div class="wordmark">
      <p class="wordmark-title">MOGP</p>
      <p class="wordmark-sub">MAVRIN OAK GUARD PATROLS</p>
    </div>

    <div class="contact">
      <p class="contact-name">ALEX MERCER</p>
      <ul class="contact-list">
        <li class="contact-item"><span class="contact-icon"></span>MOBILE NUMBER</li>
        <li class="contact-item"><span class="contact-icon"></span>EMAIL ADDRESS</li>
        <li class="contact-item"><span class="contact-icon"></span>WEBSITE EMAIL ADDRESS</li>
        <li class="contact-item"><span class="contact-icon contact-icon--none"></span>PO BOX ADDRESS</li>
      </ul>
    </div>

    <svg class="base-stripes" viewBox="0 0 479 32" aria-hidden="true">
      <rect x="0" y="0" width="479" height="32" fill="var(--ink-black)"/>
      <polygon points="0,1 238,1 244,9 0,9" fill="var(--stripe-grey)"/>
      <polygon points="238,1 479,1 479,9 244,9" fill="var(--white)"/>
    </svg>
  </section>

</main>
</body>
</html>
```